Lena Hartwell Web

Lena Hartwell is a singer/songwriter that has a presence in the market for over 20 years. She currently has a website, lenahartwell.example that needs a major makeover. IT needs to be reorganized to; 1) make it more user friendly; 2) enable multi-languages including; Spanish, French, Russian, Japanese, Chinese and Portuguese; 3) enable purchases online through a storefront of promotional merchandise and music tracks. She has a logo that needs an update, as well as we currently have a business card open on PixelBazaar for input. Working to re-brand, or refresh her brand.

Lena Hartwell is the next Rosa Delmont! She has 5 platinum records, Lumen Award nominations and tours with Harold Prescott globally and is Nora Vandermeer's key backup singer for 12 years.
Updates

Some common questions have come up.  Here is some further input:

1) Colors - No specific color in mind but probably earth tones.  Although at this point we''re completely open.  Mary likes classical style, Russian, French decor.  Paris architecture. Greek, Italian textures, Goddess like symbols from the Roman Empire, or the symbols and pomp of the British monarchy.  One name on tap for the new CD is "Lanterns Over Quiet Water"
2) Example website - I have not found a new one specifically, but what I don''t like about the existing one is it is not easy to navigate.  Needs to be streamlined and easy to navigate with a storefront for merchandise and music downloads.  
3) On Logo - We''re revamping a "Global" merchandise rollout logo.  We''ve also considered possibly modifying the old english "Hartwell" family crest which signifies royalty, but have not explored that too much.  The hexagon yellow logo on her current website, I was thinking of modifying to gold (brushed - or polished?), then taking the LH lettering using a fountain pen type look there the line thickness flows with pressure on the pen, then make the gold look like a pillow, with the letter making an impression into the gold pillow.  This expands to a high quality pin, blinged up broach with diamonds imbedded for example, Global label identity, tee shirts, label tag on fashion clothing etc etc. 
 4) One thing marketing has asked us to build is a routine video blog to reach out to fans in a personal way.  Short clips of daily activity, travel prep for shows, etc. Possibly a signup/fanpage where people get emails sent back whenever anything new is posted, like a video blog, new pics, new events.  A menu to choose what you get updates on. 

Thanks, Dennis

Target Market(s)

1) Fan base in Europe, Asia, Latin America and North America
2) Movie producers seeking soundtracks
3) Private clients seeking an outstanding performer for corporate events

Industry/Entity Type

Singer

Requirements
Must have
• Better organization into smaller pages. Items critical include: 1) music tracks, 2) ClipStream links, 3) photos & Video, 4) storefront to enable online merchandise purchase 5) a way to illustrate her genre from; gospel, to rock, funk, R&B, country,

```html
<!DOCTYPE html>
<html lang="en">
<head>
<meta charset="utf-8">
<title>Lena Hartwell</title>
<link rel="stylesheet" href="https://fonts.googleapis.com/css2?family=Open+Sans:wght@400;600&family=Oswald:wght@300;400;500&display=swap">
<style>
:root{
  --bg-deep:#1a1320;
  --bg-plum:#3a2440;
  --pink:#d11f6e;
  --pink-soft:#e0307a;
  --orange:#f08a3a;
  --orange-line:#e0702c;
  --cream:#f3e7cf;
  --muted:#7a4a7a;
  --white:#ffffff;
  --gold:#f2d43a;
}
*{box-sizing:border-box;margin:0;padding:0}
html,body{width:1013px;height:1200px;overflow:hidden;background:var(--bg-deep)}
body{font-family:"Oswald",sans-serif;color:var(--cream)}
.canvas{position:relative;width:1013px;height:1200px;overflow:hidden}
.backdrop{position:absolute;inset:0;
  background:
    radial-gradient(ellipse 320px 600px at 80px 600px,rgba(80,60,70,.55),transparent 70%),
    radial-gradient(ellipse 500px 300px at 850px 1050px,rgba(70,70,75,.35),transparent 70%),
    linear-gradient(180deg,#2a1a30 0%,#3c2344 28%,#2a1c2e 55%,#1e1a1e 100%);}
.nav{position:absolute;top:30px;left:0;width:100%;font-family:"Open Sans",sans-serif;font-size:14.5px;font-weight:600;color:var(--pink)}
.nav a{position:absolute;color:inherit;text-decoration:none;letter-spacing:.2px}
.hero{position:absolute;left:123px;top:68px;width:758px;height:233px;border:2px solid var(--white);
  background:linear-gradient(90deg,#8a5a2c 0%,#b97a3e 25%,#6a4a40 45%,#c08846 70%,#8a5e34 100%)}
.hero-arrow{position:absolute;top:105px}
.hero-mark{position:absolute;right:10px;bottom:22px;display:flex;align-items:center;gap:5px;font-family:"Oswald",sans-serif;font-size:18px;font-weight:500;color:var(--gold)}
.hero-mark i{display:block;width:12px;height:12px;border-radius:50%;background:var(--gold)}
.dots{position:absolute;left:355px;bottom:8px;display:flex;gap:13px;align-items:center}
.dots span{width:11px;height:11px;border-radius:50%;border:2px solid #fff;background:#2b1540}
.dots span.on{width:14px;height:14px;background:var(--pink)}
.player{position:absolute;left:140px;top:356px;width:160px;height:80px}
.album{position:absolute;left:0;top:0;width:52px;height:54px;border:2px solid #bbb;background:linear-gradient(160deg,#c7d0cc,#5c6a66)}
.track{position:absolute;left:83px;top:3px;font-family:"Open Sans",sans-serif;font-size:8px;color:var(--pink-soft)}
.track small{display:block;color:var(--cream);font-size:6.5px;margin-top:3px}
.share{position:absolute;left:81px;top:29px;background:var(--pink);color:#fff;font-family:"Open Sans",sans-serif;font-size:6px;padding:3px 5px}
.stars{position:absolute;left:117px;top:27px;font-size:9px;color:var(--gold);letter-spacing:1px}
.time{position:absolute;left:38px;top:62px;font-family:"Open Sans",sans-serif;font-size:6px;background:#222;color:#fff;padding:1px 3px}
.progress{position:absolute;left:0;top:74px;width:80px;height:3px;background:#555}
.progress b{display:block;width:52px;height:3px;background:var(--pink)}
.controls{position:absolute;left:92px;top:52px}
.heading{position:absolute;font-family:"Oswald",sans-serif;font-weight:400;font-size:21px;color:var(--pink);line-height:1;letter-spacing:.2px}
.more{position:absolute;font-size:10.5px;color:var(--orange);display:flex;align-items:center;gap:3px}
.more::after{content:"";border-left:5px solid var(--orange);border-top:3.5px solid transparent;border-bottom:3.5px solid transparent}
.follow{position:absolute;left:262px;top:469px;font-size:12px;color:var(--orange)}
.tweet{position:absolute;left:141px;width:157px;font-size:11px;line-height:12.7px;font-weight:300;color:var(--cream)}
.tweet .avatar{float:left;width:28px;height:28px;margin:0 8px 0 0;background:linear-gradient(135deg,#7a5a3a,#2a1a14)}
.tweet .handle{color:var(--orange);display:block}
.rule{position:absolute;height:2px;background:var(--orange-line)}
.fan{position:absolute;left:143px;top:908px}
.fan .mark{position:absolute;left:0;top:0;width:41px;height:41px;background:var(--white);display:flex;align-items:center;justify-content:center;font-size:15px;font-weight:500;color:var(--pink)}
.fan .name{position:absolute;left:44px;top:2px;white-space:nowrap;font-size:9px;font-weight:500;color:var(--orange)}
.fan .like{position:absolute;left:44px;top:20px;background:#4a66a8;color:#fff;font-size:8.5px;padding:1px 5px}
.fan .count{position:absolute;left:85px;top:22px;font-size:8px;color:#fff}
.subhead{position:absolute;font-size:11.5px;font-weight:400;color:var(--cream)}
.video{position:absolute;left:356px;top:386px;width:245px;height:201px;border:2px solid #fff;
  background:radial-gradient(ellipse 60px 100px at 130px 120px,#8a4a9a,transparent 80%),linear-gradient(180deg,#4a2a66,#2a1440)}
.video svg{position:absolute;left:112px;top:80px}
.tour-sub{position:absolute;left:357px;top:655px;font-size:11.5px;color:var(--cream)}
.tour-sub span{color:var(--muted);font-weight:300}
.gig{position:absolute;left:356px;width:234px;font-size:10px;color:var(--orange)}
.gig .date{position:absolute;left:19px;font-weight:300}
.gig .venue{position:absolute;left:95px;top:-2px;font-size:6.5px;line-height:8px;font-weight:500;color:var(--cream)}
.gig .tix{position:absolute;left:195px;text-decoration:underline}
.showall{position:absolute;left:375px;top:1021px;font-size:10px;color:var(--orange);text-decoration:underline;font-weight:300}
.news{position:absolute;left:652px;width:210px;font-weight:300}
.news h3{font-weight:300;font-size:10px;color:var(--pink-soft)}
.news p{font-size:10px;line-height:11.5px;color:var(--cream);margin-top:4px}
.news a{display:block;margin-top:13px;font-size:10px;color:var(--orange);text-decoration:underline}
.loadall{position:absolute;left:652px;top:873px;font-size:10px;color:var(--orange);text-decoration:underline;font-weight:300}
.footer{position:absolute;top:1174px;left:0;width:100%;text-align:center;font-family:"Open Sans",sans-serif;font-size:8.5px;color:var(--pink)}
.footer b{color:var(--orange);font-weight:600}
</style>
</head>
<body>
<div class="canvas">
  <div class="backdrop" role="img" aria-label="Dim stage photograph of the singer performing, with soft bokeh lights along the top"></div>

  <nav class="nav">
    <a style="left:204px">HOME</a>
    <a style="left:289px">EVENTS</a>
    <a style="left:381px">MUSIC</a>
    <a style="left:471px">VIDEO</a>
    <a style="left:548px">PICTURES</a>
    <a style="left:647px">ABOUT</a>
    <a style="left:725px">CONTACT</a>
  </nav>

  <section class="hero" role="img" aria-label="Portrait of the singer seated in a car with tan leather seats, wearing a fur collar">
    <svg class="hero-arrow" style="left:10px" width="14" height="22" viewBox="0 0 14 22"><path d="M12 2L3 11l9 9" fill="none" stroke="#fff" stroke-width="3"/></svg>
    <svg class="hero-arrow" style="right:10px" width="14" height="22" viewBox="0 0 14 22"><path d="M2 2l9 9-9 9" fill="none" stroke="#fff" stroke-width="3"/></svg>
    <div class="hero-mark"><i></i>LH</div>
    <div class="dots"><span></span><span></span><span class="on"></span><span></span><span></span></div>
  </section>

  <div class="player">
    <div class="album" role="img" aria-label="Album cover artwork"></div>
    <div class="track">Silver Harbor<small>Collected Songs 1990-2000</small></div>
    <div class="share">Share</div>
    <div class="stars">★★★</div>
    <div class="time">3:43/4:56</div>
    <div class="progress"><b></b></div>
    <svg class="controls" width="68" height="26" viewBox="0 0 68 26">
      <circle cx="8" cy="13" r="7.5" fill="#c8487e"/><path d="M8 9l-4 4 4 4zM12 9l-4 4 4 4z" fill="#fff"/>
      <circle cx="34" cy="13" r="12" fill="#c8487e"/><path d="M30 7v12l10-6z" fill="#3a1430"/>
      <circle cx="60" cy="13" r="7.5" fill="#c8487e"/><path d="M56 9l4 4-4 4zM60 9l4 4-4 4z" fill="#fff"/>
    </svg>
  </div>

  <h2 class="heading" style="left:135px;top:464px">CHIRPER</h2>
  <span class="follow">Follow</span>

  <div class="tweet" style="top:502px"><span class="avatar" role="img" aria-label="Profile photo"></span><span class="handle">@lenahartwellsing</span>Good evening friends! I hope your having a great week so far, remember I love you.</div>
  <div class="rule" style="left:140px;top:563px;width:152px"></div>
  <div class="tweet" style="top:574px"><span class="avatar" role="img" aria-label="Profile photo"></span><span class="handle">@lenahartwellsing</span>Panama night life is beautiful</div>
  <div class="rule" style="left:140px;top:621px;width:152px"></div>
  <div class="tweet" style="top:632px"><span class="avatar" role="img" aria-label="Profile photo"></span><span class="handle">@lenahartwellsing</span>The Opera House in Panama</div>
  <div class="rule" style="left:140px;top:679px;width:152px"></div>
  <div class="tweet" style="top:692px"><span class="avatar" role="img" aria-label="Profile photo"></span><span class="handle">@lenahartwellsing</span>Hello friends I hope your week is off to a great start! Just remember everyone has inside of them a piece of good...</div>
  <div class="rule" style="left:140px;top:769px;width:152px"></div>
  <div class="tweet" style="top:784px"><span class="avatar" role="img" aria-label="Profile photo"></span><span class="handle">@lenahartwellsing</span>Singing is what I do and I Love it......Thank you Joey Castellan for the photos</div>
  <div class="rule" style="left:140px;top:847px;width:152px"></div>

  <h2 class="heading" style="left:135px;top:870px">SOCIALHUB</h2>
  <div class="fan">
    <div class="mark">LH</div>
    <div class="name">LENA HARTWELL FANPAGE</div>
    <div class="like">Like</div>
    <div class="count">2,314</div>
  </div>

  <h2 class="heading" style="left:357px;top:343px">FEATURED MEDIA</h2>
  <span class="more" style="left:568px;top:348px">more</span>
  <div class="subhead" style="left:357px;top:365px">LENA HARTWELL AT THE HALL OF ECHOES</div>
  <div class="video" role="img" aria-label="Concert video still of the singer performing on stage in a sequined dress">
    <svg width="40" height="50" viewBox="0 0 40 50"><path d="M4 3q0-3 3-1l30 20q3 3 0 6L7 48q-3 2-3-1z" fill="#fff"/></svg>
  </div>

  <h2 class="heading" style="left:357px;top:632px">TOUR DATES</h2>
  <span class="more" style="left:568px;top:637px">more</span>
  <div class="tour-sub">UPCOMING | <span>LOCAL DATES</span></div>

  <div class="rule" style="left:356px;top:690px;width:234px"></div>
  <div class="gig" style="top:710px"><span class="date">Jan 04</span><span class="venue">Meridian Plaza Hotel<br>Topeka, KS</span><span class="tix">Tickets</span></div>
  <div class="rule" style="left:356px;top:743px;width:234px"></div>
  <div class="gig" style="top:764px"><span class="date">Jan 15</span><span class="venue">The Foundry<br>Summit, MS</span><span class="tix">Tickets</span></div>
  <div class="rule" style="left:356px;top:796px;width:234px"></div>
  <div class="gig" style="top:818px"><span class="date">May 24</span><span class="venue">Tidewater<br>Kihei, HI</span><span class="tix">Tickets</span></div>
  <div class="rule" style="left:356px;top:849px;width:234px"></div>
  <div class="gig" style="top:870px"><span class="date">May 25</span><span class="venue">Tidewater<br>Kihei, HI</span><span class="tix">Tickets</span></div>
  <div class="rule" style="left:356px;top:902px;width:234px"></div>
  <div class="gig" style="top:925px"><span class="date">May 26</span><span class="venue">Tidewater<br>Kihei, HI</span><span class="tix">Tickets</span></div>
  <div class="rule" style="left:356px;top:956px;width:234px"></div>
  <div class="gig" style="top:979px"><span class="date">May 27</span><span class="venue">Tidewater<br>Kihei, HI</span><span class="tix">Tickets</span></div>
  <div class="rule" style="left:356px;top:1008px;width:234px"></div>
  <span class="showall">Show All Dates</span>
  <div class="rule" style="left:356px;top:1044px;width:234px"></div>

  <h2 class="heading" style="left:652px;top:343px">NEWS &amp; BLOG</h2>
  <span class="more" style="left:841px;top:348px">more</span>

  <article class="news" style="top:380px"><h3>Lena Hartwell Band</h3><p>They have blessed me with their gift and give me the opportunity to do what I do best.</p><a>Read More</a></article>
  <div class="rule" style="left:652px;top:455px;width:203px"></div>
  <article class="news" style="top:477px"><h3>Court Legends Red Carpet Gala</h3><p>Im headlining the Court Legends Red Carpet Gala All Star Weekend Event.</p><a>Read More</a></article>
  <div class="rule" style="left:652px;top:554px;width:203px"></div>
  <article class="news" style="top:576px"><h3>Heritage Folk Life Festival</h3><p>A wonderful gig with Harold Prescott and The Velvet Circuit in Washington DC.</p><a>Read More</a></article>
  <div class="rule" style="left:652px;top:655px;width:203px"></div>
  <article class="news" style="top:675px"><h3>Riverside Summer Pride</h3><p>next performance will be at the Riverside Summer Pride on June 24th in Fort Lauderdale, Florida.</p><a>Read More</a></article>
  <div class="rule" style="left:652px;top:755px;width:203px"></div>
  <article class="news" style="top:778px"><h3>Luminary Magazine</h3><p>Interview in the new magazine "LUMINARY" it is available online on April 5th.</p><a>Read More</a></article>
  <div class="rule" style="left:652px;top:860px;width:203px"></div>
  <span class="loadall">Load All News &amp; Blog</span>
  <div class="rule" style="left:652px;top:891px;width:203px"></div>

  <footer class="footer">© 2011, Lena Hartwell All rights reserved. <b>| Contact</b></footer>
</div>
</body>
</html>
```